Veteran Owned General Contractor needs Bold New Business Cards

We are a service disabled veteran owned small business. We're a general contractor that specializes in excavation, underground utilities, site work, land clearing and demolition. We would like a fresh, simple, bold, new look for our business cards. We're open to ideas! We'd like to incorporate the following information on the card:

Company Name & Logo, Name of Person, Job Title, Office Phone, Fax, Cell Phone, Email Address, Website, SDVOSB

Our logo is included. We look forward to your thoughts.

Thank you!

Reason: Hello Due to the overwhelming response to this project, we are extending the deadline one time to allow for improved communication and feedback with the top candidates. We would like to thank everyone for their hard work and exceptional creativity! Thank you

Industry/Entity Type

Business

Contact Information for Business Card

Font styles to use
Sans Serif

Requirements
Nice to have
• As we are a veteran owned company, it would be nice to incorporate an American flag into the design. Maybe on the back?

```html
<!DOCTYPE html>
<html lang="en">
<head>
<meta charset="utf-8">
<title>Ironside Works Inc. — Business Card</title>
<link href="https://fonts.googleapis.com/css2?family=Open+Sans:wght@400;600;700;800&display=swap" rel="stylesheet">
<style>
  :root {
    --bg: #2b2b2b;
    --card-white: #ffffff;
    --card-black: #161616;
    --green: #5fbf3c;
    --ink: #3a3a3a;
    --ink-soft: #555555;
  }
  * { margin: 0; padding: 0; box-sizing: border-box; }
  html, body {
    width: 1200px; height: 1000px; overflow: hidden;
    background: var(--bg);
    font-family: "Open Sans", Arial, sans-serif;
  }
  .sheet { position: relative; width: 1200px; height: 1000px; }
  .card {
    position: absolute; left: 300px;
    width: 600px; height: 343px;
    border-radius: 26px; overflow: hidden;
    box-shadow: 0 10px 30px rgba(0,0,0,.45);
  }
  .card-back { top: 110px; background: var(--card-black); }
  .card-front { top: 540px; background: var(--card-white); }

  .wordmark {
    position: absolute;
    font-family: "Open Sans", Arial, sans-serif;
    font-weight: 800; color: var(--green);
    letter-spacing: 1px; white-space: nowrap; line-height: 1;
  }
  .card-back .wordmark {
    left: 50%; top: 50%;
    transform: translate(-50%, -50%);
    font-size: 48px;
  }
  .card-front .wordmark { right: 34px; top: 40px; font-size: 20px; }

  .edge-tab { position: absolute; width: 14px; background: var(--green); }
  .edge-tab-right { right: 0; top: 82px; height: 100px; border-radius: 14px 0 0 14px; }
  .edge-tab-left { left: 0; top: 258px; height: 85px; border-radius: 0 14px 0 0; }

  .person { position: absolute; left: 40px; top: 150px; }
  .person-name { font-size: 22px; font-weight: 700; color: var(--ink); letter-spacing: .5px; }
  .person-name .surname { color: var(--green); }
  .person-title { margin-top: 2px; font-size: 12px; font-weight: 600; color: var(--ink-soft); letter-spacing: 1px; }

  .address {
    position: absolute; right: 38px; top: 178px; text-align: right;
    font-style: normal;
    font-size: 12.5px; line-height: 1.45; color: var(--ink-soft);
  }
  .address .company { color: var(--green); font-weight: 600; }

  .contacts {
    position: absolute; left: 40px; top: 236px; list-style: none;
    font-size: 12.5px; color: var(--ink); line-height: 1;
  }
  .contacts li { display: flex; align-items: center; gap: 9px; height: 17px; }
  .contacts svg { width: 12px; height: 12px; fill: var(--green); flex: none; }
  .contacts .accent { color: var(--green); }
</style>
</head>
<body>
<main class="sheet">

  <section class="card card-back" aria-label="Card back">
    <div class="wordmark">IRONSIDE WORKS</div>
  </section>

  <section class="card card-front" aria-label="Card front">
    <div class="wordmark">IRONSIDE WORKS</div>
    <span class="edge-tab edge-tab-right"></span>
    <span class="edge-tab edge-tab-left"></span>

    <div class="person">
      <p class="person-name">DANIEL <span class="surname">BROOKS</span></p>
      <p class="person-title">FOUNDER</p>
    </div>

    <address class="address">
      <span class="company">Ironside Works Inc.</span><br>
      your street address,<br>
      suite-123, country-1230
    </address>

    <ul class="contacts">
      <li>
        <svg viewBox="0 0 12 12"><path d="M1 4c0-2 2-3 5-3s5 1 5 3l-2 1-1-1V3H4v1L3 5zM2 6h8l1 5H1z"/></svg>
        <span>000 000 0000</span>
      </li>
      <li>
        <svg viewBox="0 0 12 12"><path d="M2 1l2-.5 1.5 3-1.2 1a7 7 0 0 0 3.2 3.2l1-1.2 3 1.5-.5 2C6 11 1 6 2 1z"/></svg>
        <span>000 000 0000</span>
      </li>
      <li>
        <svg viewBox="0 0 12 12"><path d="M3 1h5v3H3zM1 5h10v6H1zM3 7h2v1H3zm4 0h2v1H7z"/></svg>
        <span>000 000 0000</span>
      </li>
      <li>
        <svg viewBox="0 0 12 12"><path d="M0 2h12v1L6 7 0 3zM0 4.5l6 4 6-4V10H0z"/></svg>
        <span>info@yourmail.com</span>
      </li>
      <li>
        <svg viewBox="0 0 12 12"><path d="M7 0a5 5 0 1 1-3.6 8.5L.8 11.2 0 10.4l2.7-2.6A5 5 0 0 1 7 0zm0 1.6a3.4 3.4 0 1 0 0 6.8 3.4 3.4 0 0 0 0-6.8z"/></svg>
        <span>www.<span class="accent">yoursite</span>.com</span>
      </li>
    </ul>
  </section>

</main>
</body>
</html>
```